Equipment financing with a focus on truck financing, need a business card

Looking to get a business card designed that stands out to represent my financing company. Vorlin Truck & Equipment Financing. Even though I can finance all types of equipment my main focus will be on trucks. I can do financing all across Canada.I liked the design on the one I attached for Harrowmere Funding Corp.I want a truck picture to be on the card like the Brisket Monetary card (this is not my company, it is someone elses and I've attached it as a sample) . If you can add a construction piece of equipment as well that would be great, something along the lines of the attachment for Brisket Monetary. I want the Khanda symbol as well on the card, it can be one color if you choose, I thought something like the attachment stood out more. The Khanda is a symbol of Sikh faith. I am targeting most of my business to Sikh truck drivers. Card should have a black background so it stands out. It can be horizontal or vertical or a combination of both.Thinking the front of the card has a larger Khanda symbol and then a smaller one inside of it and then my name Vorlin Truck & Equipment Financing .
Target Market(s)
Deal with people in all types of industries
Industry/Entity Type
Finance
Contact Information for Business Card
The front could be split black and other colors to make the khanda and lettering pop out. Open to any type of design.
Back of card would say
President
Ravi Tomlin
Mobile
403 555 0142
Email
Ravi.Vorlinto@quessmoorfunds.example
at the bottom like the Harrowmere Funding Corp card I want it to say and stand out
EQUIPMENT FINANCE SPECIALIST
am open to anything that looks great and stands out, modern and bold.
Colors
Designer to choose colors to be used in the design.
Requirements
Must have
- I would like the color of the khanda symbol to be similar to the picture I attached, kind of a goldish color, make the letters in a similar color as well
- - Modern
- - Different
- - Stand Out
- - Makes an Impression
Nice to have
- In summary, Brisket Monetary is not my logo nor my business name its. I would like something similar though with a truck on the card, and if there is a way perhaps a piece of construction equipment.
- VORLIN TRUCK & EQUIPMENT FINANCING is the name of my company.
- I want a card that stands out and is bold like the Harrowmere Funding Corp card I attached
- The Khanda is a sikh symbol, I attached a pic of what it looks like.

```html
<!DOCTYPE html>
<html lang="en">
<head>
<meta charset="utf-8">
<title>Vorlin Truck &amp; Equipment Financing — Business Card</title>
<link rel="stylesheet" href="https://fonts.googleapis.com/css2?family=Open+Sans:wght@400;600;700;800&display=swap">
<style>
  :root {
    --stage: #333333;
    --card: #000000;
    --gold: #9b7c2e;
    --gold-text: #9a7b2c;
    --gold-deep: #67552f;
    --gold-line: #b8984a;
    --white: #ffffff;
  }
  * { margin: 0; padding: 0; box-sizing: border-box; }
  html, body {
    width: 1200px; height: 1000px; overflow: hidden;
    background: var(--stage);
    font-family: "Open Sans", Arial, sans-serif;
  }
  .stage { position: relative; width: 1200px; height: 1000px; }
  .card {
    position: absolute; top: 114px; width: 440px; height: 772px;
    background: var(--card);
    box-shadow: 0 24px 50px rgba(0,0,0,.45);
    overflow: hidden;
  }
  .card--front { left: 120px; }
  .card--back { left: 640px; }

  .khanda-emblem {
    position: absolute; left: 130px; top: 64px; width: 180px; height: 220px;
    border-radius: 50% 50% 40% 40%;
    background: radial-gradient(circle at 50% 40%, #c9a24c 0%, #8a6a26 55%, rgba(60,45,15,0) 75%);
  }
  .name-band { position: absolute; left: 0; top: 338px; width: 440px; height: 324px; }
  .name-band svg { display: block; }
  .holder-name {
    position: absolute; left: 0; right: 0; top: 394px;
    text-align: center; color: var(--white);
    font-size: 38px; font-weight: 700; letter-spacing: .5px;
  }
  .holder-title {
    position: absolute; left: 0; right: 0; top: 450px;
    text-align: center; color: var(--white);
    font-size: 26px; font-weight: 400;
  }
  .divider {
    position: absolute; left: 0; width: 440px; height: 1px;
    background: var(--gold-line);
  }
  .divider--one { top: 517px; }
  .divider--two { top: 589px; }
  .contact {
    position: absolute; left: 0; right: 0;
    display: flex; align-items: center; justify-content: center; gap: 14px;
    color: var(--white); font-size: 18px;
  }
  .contact--phone { top: 541px; }
  .contact--email { top: 611px; }
  .contact svg { flex: none; }
  .specialty {
    position: absolute; left: 0; right: 0; top: 700px;
    text-align: center; color: var(--gold-text);
    font-size: 20px; font-weight: 700; letter-spacing: .3px;
  }

  .truck-art {
    position: absolute; left: 10px; top: 52px; width: 430px; height: 480px;
    border-radius: 60% 0 0 30% / 40% 0 0 20%;
    background: linear-gradient(160deg, #6d5a31 0%, var(--gold-deep) 60%, #3a3019 100%);
  }
  .wordmark {
    position: absolute; left: 190px; top: 622px;
    color: var(--gold-text); font-weight: 700;
  }
  .wordmark__name { display: block; font-size: 44px; line-height: 1; letter-spacing: 2px; }
  .wordmark__line { display: block; font-size: 10.5px; margin-top: 6px; letter-spacing: .3px; }
  .wordmark-dot {
    position: absolute; left: 112px; top: 626px; width: 62px; height: 62px;
    border-radius: 50%; background: var(--gold-text);
  }
</style>
</head>
<body>
<main class="stage">
  <section class="card card--front">
    <div class="khanda-emblem" role="img" aria-label="Gold embossed Khanda symbol"></div>

    <div class="name-band">
      <svg width="440" height="324" viewBox="0 0 440 324" aria-hidden="true">
        <path fill="#9b7c2e" d="M0 32 H26 C40 18 50 2 80 0 H360 C390 2 400 18 414 32 H440 V324 H0 Z"/>
      </svg>
    </div>

    <h1 class="holder-name">RAVI TOMLIN</h1>
    <p class="holder-title">President</p>

    <div class="divider divider--one"></div>
    <p class="contact contact--phone">
      <svg width="18" height="18" viewBox="0 0 18 18" aria-hidden="true">
        <rect width="18" height="18" rx="3" fill="#fff"/>
        <path fill="#9b7c2e" d="M5.2 3.5l2 2.1-1.1 1.5c.8 1.7 2 2.9 3.8 3.8l1.5-1.1 2.1 2-1.2 2.2C8.3 13.8 4.2 9.7 3.9 4.7z"/>
      </svg>
      <span>403 555 0142</span>
    </p>
    <div class="divider divider--two"></div>
    <p class="contact contact--email">
      <svg width="20" height="15" viewBox="0 0 20 15" aria-hidden="true">
        <rect width="20" height="15" rx="1.5" fill="#fff"/>
        <path d="M1 1.5l9 7 9-7" fill="none" stroke="#9b7c2e" stroke-width="1.6"/>
      </svg>
      <span>Ravi.Vorlinto@quessmoorfunds.example</span>
    </p>

    <p class="specialty">EQUIPMENT FINANCE SPECIALIST</p>
  </section>

  <section class="card card--back">
    <div class="truck-art" role="img" aria-label="Gold silhouette of a semi truck front with a sweeping road curve"></div>
    <span class="wordmark-dot" aria-hidden="true"></span>
    <p class="wordmark">
      <span class="wordmark__name">VORLIN</span>
      <span class="wordmark__line">TRUCK &amp; EQUIPMENT FINANCING</span>
    </p>
  </section>
</main>
</body>
</html>
```